I need a book cover design for my book "Roaming Quartets." It is a non-fiction book focused on answering the question of whether American evangelicals look more like the Quartets than Jesus.

The subtitle is "The Curious Habits of Norway's Traveling Fiddlers and Their Seaside Rivals." The author name is Dorian Whitlock.

I will be publishing this as an ebook and paperback.

I am open to all ideas, but will share the only thought I had as a possible design. In the title, the third letter in both words is "A." I thought about the idea of having the "A" in "Roaming" have a halo and the "A" in "Quartets" somehow seem to be a shadow of that first "A" but have devil horns instead of a halo. Again, I'm not sold on that, but am sharing it as one design possibility.

I am not interested in the book cover design having a cheesy religious look to it (as many do). I am more interested in it looking like a professional non-fiction cover.

```html
<!DOCTYPE html>
<html lang="en">
<head>
<meta charset="utf-8">
<title>Roaming Quartets — Book Cover</title>
<link rel="stylesheet" href="https://fonts.googleapis.com/css2?family=Open+Sans:wght@400&family=Playfair+Display:ital,wght@1,700&display=swap">
<style>
  :root {
    --page-bg: #1a1714;
    --title-white: #ffffff;
    --subtitle-white: rgba(255, 255, 255, 0.86);
    --author-gold: #d8901c;
    --glow-gold: #c9a04a;
    --mist-olive: #6d6a45;
    --shade-dark: #1f211c;
    --mist-teal: #7d8f8c;
    --grass-dark: #141a10;
  }
  html, body {
    margin: 0;
    padding: 0;
    width: 1200px;
    height: 800px;
    overflow: hidden;
    background: var(--page-bg);
  }
  .canvas {
    position: relative;
    width: 1200px;
    height: 800px;
    display: flex;
    align-items: center;
    justify-content: center;
  }
  .book-cover {
    position: relative;
    width: 508px;
    height: 740px;
    overflow: hidden;
    box-shadow: 0 10px 40px rgba(0, 0, 0, 0.6);
  }
  .cover-art {
    position: absolute;
    inset: 0;
    width: 100%;
    height: 100%;
    display: block;
  }
  .book-title {
    margin: 0;
    font-weight: 400;
  }
  .title-word {
    position: absolute;
    display: block;
    font-family: "Open Sans", sans-serif;
    font-weight: 400;
    font-size: 86px;
    line-height: 1;
    letter-spacing: 0.01em;
    color: var(--title-white);
    writing-mode: vertical-rl;
    white-space: nowrap;
    text-transform: uppercase;
  }
  .title-word--first {
    left: 39.5%;
    bottom: 24.2%;
    transform: translateX(-50%) rotate(180deg);
  }
  .title-word--second {
    left: 63.5%;
    top: 6.3%;
    transform: translateX(-50%);
  }
  .subtitle {
    position: absolute;
    left: 50%;
    top: 81.5%;
    width: 380px;
    transform: translateX(-50%);
    margin: 0;
    font-family: "Open Sans", sans-serif;
    font-weight: 400;
    font-size: 13px;
    line-height: 1.45;
    letter-spacing: 0.04em;
    text-align: center;
    color: var(--subtitle-white);
  }
  .author-name {
    position: absolute;
    left: 53%;
    top: 94%;
    transform: translate(-50%, -50%);
    margin: 0;
    font-family: "Playfair Display", serif;
    font-style: italic;
    font-weight: 700;
    font-size: 22px;
    color: var(--author-gold);
    white-space: nowrap;
  }
</style>
</head>
<body>
  <main class="canvas">
    <article class="book-cover">
      <svg class="cover-art" viewBox="0 0 508 740" preserveAspectRatio="none" role="img" aria-label="Photograph of a misty forest with tall tree trunks backlit by warm golden light, fading to cool grey mist on the right, over a dark meadow of dandelions">
        <defs>
          <linearGradient id="forest-light" x1="0" y1="0" x2="1" y2="0">
            <stop offset="0" stop-color="var(--glow-gold)"/>
            <stop offset="0.3" stop-color="var(--mist-olive)"/>
            <stop offset="0.5" stop-color="var(--shade-dark)"/>
            <stop offset="0.75" stop-color="var(--mist-teal)"/>
            <stop offset="1" stop-color="var(--shade-dark)"/>
          </linearGradient>
          <linearGradient id="meadow-shade" x1="0" y1="0" x2="0" y2="1">
            <stop offset="0" stop-color="#000" stop-opacity="0.35"/>
            <stop offset="0.35" stop-color="#000" stop-opacity="0"/>
            <stop offset="0.76" stop-color="#000" stop-opacity="0"/>
            <stop offset="0.84" stop-color="var(--grass-dark)" stop-opacity="0.9"/>
            <stop offset="1" stop-color="var(--grass-dark)" stop-opacity="1"/>
          </linearGradient>
        </defs>
        <rect width="508" height="740" fill="url(#forest-light)"/>
        <rect width="508" height="740" fill="url(#meadow-shade)"/>
      </svg>
      <h1 class="book-title">
        <span class="title-word title-word--first">Roaming</span>
        <span class="title-word title-word--second">Quartets</span>
      </h1>
      <p class="subtitle">The Curious Habits of Norway's Traveling Fiddlers and Their Seaside Rivals</p>
      <p class="author-name">Dorian Whitlock</p>
    </article>
  </main>
</body>
</html>
```